business card design - photography

I am a fine art photographer. I would like to approach galleries to exhibit my work and need a business card.

The card should convey creativity and simplicity.
I would like a double sided card.

Some options:
1. An all white card with raised or embossed text or design to create a tactile finish.
2. a white and dark grey design would also work well.
3. Would be great to use my name as part of the design but not essential.
4. My name and title on the front, other details on the back of card.

The final design should be simple, minimal, elegant and innovative.
Being minimal, it will be more about texture, text size and placement.

examples of designs I would prefer provided here:
http://plimvarka.com/ideas/40-quiet-and-refined-card-layouts

I'm also open to other designs that may be unusual and unique.

Love this:
http://www.snapvelo.com/pics/morningverselog/583014927
Updates

I have uploaded a psd file after playing around in photoshop with various fonts.  I like the font (which I downloaded from glyphmorra.com called Arual) but the design probably needs some refining.  I hope this helps.  If you'd like me to change the format of the file, please let me know.

Ilvane

Target Market(s)

Art Gallery owners/administrators and customers.

Industry/Entity Type

Business

Requirements
Must have
• A unique look.

Matte, silky finish or heavy textured stock. Double-sided card.

Front:
my name
photography by

Back:
phone no
email
web address
Nice to have
• Letterpress
embrossed
Clean fonts
Should not have
• Do not use illustrations of cameras or lenses.
No frames around the card edge.

```html
<!DOCTYPE html>
<html lang="en">
<head>
<meta charset="utf-8">
<title>Ilvane Ravell Photography – Business Card</title>
<link rel="stylesheet" href="https://fonts.googleapis.com/css2?family=Cinzel:wght@500&family=Montserrat:ital,wght@0,600;0,700;1,600;1,700&display=swap">
<style>
  :root {
    --page-bg: #ffffff;
    --stock-light: #f1f1f0;
    --stock-mid: #e4e4e3;
    --ink-blue: #3c4c9e;
    --ink-grey: #3a3a3c;
  }
  * { margin: 0; padding: 0; box-sizing: border-box; }
  html, body {
    width: 1200px;
    height: 644px;
    overflow: hidden;
    background: var(--page-bg);
  }
  .canvas {
    position: relative;
    width: 1200px;
    height: 644px;
  }
  .card {
    position: absolute;
    top: 171px;
    width: 532px;
    height: 302px;
    background: radial-gradient(ellipse at 40% 40%, var(--stock-light), var(--stock-mid));
    overflow: hidden;
  }
  .card--front { left: 52px; }
  .card--back { left: 616px; }

  .wordmark {
    position: absolute;
    color: var(--ink-blue);
    font-family: "Cinzel", serif;
    font-weight: 500;
    white-space: nowrap;
    line-height: 1;
  }
  .tagline {
    position: absolute;
    display: flex;
    align-items: center;
    gap: 5px;
    color: var(--ink-grey);
    font-family: "Montserrat", sans-serif;
    font-weight: 700;
    text-transform: uppercase;
    white-space: nowrap;
    line-height: 1;
  }
  .tagline__dot {
    border: 1.5px solid var(--ink-grey);
    border-radius: 50%;
  }

  /* front */
  .card--front .wordmark {
    left: 36px;
    top: 100px;
    font-size: 56px;
  }
  .card--front .tagline {
    right: 38px;
    top: 176px;
    font-size: 15px;
    letter-spacing: 0.5px;
  }
  .card--front .tagline__dot { width: 11px; height: 11px; }

  /* back */
  .card--back .wordmark {
    left: 30px;
    top: 244px;
    font-size: 27px;
  }
  .card--back .tagline {
    left: 148px;
    top: 276px;
    font-size: 8px;
    letter-spacing: 0.3px;
  }
  .card--back .tagline__dot { width: 7px; height: 7px; border-width: 1px; }

  .contact {
    position: absolute;
    left: 304px;
    top: 248px;
    list-style: none;
    color: var(--ink-grey);
    font-family: "Montserrat", sans-serif;
    font-style: italic;
    font-size: 10.5px;
    font-weight: 700;
    text-transform: uppercase;
    letter-spacing: 0.4px;
    line-height: 13px;
    white-space: nowrap;
  }
  .contact__label { font-weight: 600; }
</style>
</head>
<body>
  <main class="canvas">
    <section class="card card--front" role="img" aria-label="Front of card on white leather-grain textured stock">
      <div class="wordmark">Ilvane Ravell</div>
      <div class="tagline"><span class="tagline__dot"></span>Photography</div>
    </section>

    <section class="card card--back" role="img" aria-label="Back of card on white leather-grain textured stock">
      <div class="wordmark">Ilvane Ravell</div>
      <div class="tagline"><span class="tagline__dot"></span>Photography</div>
      <ul class="contact">
        <li><span class="contact__label">Phone:</span> 0412 580 327</li>
        <li><span class="contact__label">Email:</span> iravell@mailfen.com</li>
        <li><span class="contact__label">Website:</span> www.ilvaneravell.com</li>
      </ul>
    </section>
  </main>
</body>
</html>
```